Flyer for customer acquisition.

Hello, We are a sportmanagement agency from Germany and we need information flyers for customer acquisition. It should be DinA4 and should have a modern but serious design. I have uploaded a information sheet, where you can find the text and the composition, the flyer should have. I also uploaded Pictures / Images, which you can use. Of course you can use other suitable images. If they are not free, I will buy them later. On the bottom of the flyer there has been the contact information. You will find them in the download section, too. If you have questions, just write me. If I forgot something, I will update the letter :) Thank you very much!
Ich brauche zusätzliche Tage um durchzusehen

```html
<!DOCTYPE html>
<html lang="de">
<head>
<meta charset="utf-8">
<title>VELKOR – Nachwuchsförderung</title>
<link rel="stylesheet" href="https://fonts.googleapis.com/css2?family=Lato:wght@400;700&display=swap">
<style>
  :root{
    --blue:#0aa2d6;
    --dark:#262626;
    --text:#333333;
    --grey-band:#dcdcdc;
    --frame:#bdbdbd;
    --page:#ffffff;
    --stage:#e6e6e6;
  }
  *{box-sizing:border-box;margin:0;padding:0}
  html,body{width:1200px;height:1200px;overflow:hidden;background:var(--stage);font-family:"Lato",sans-serif;color:var(--text)}
  .flyer{position:absolute;left:176px;top:5px;width:848px;height:1190px;background:var(--page);overflow:hidden;box-shadow:0 2px 10px rgba(0,0,0,.15)}
  .top-wash{position:absolute;left:0;top:0;width:848px;height:440px;background:linear-gradient(180deg,#f0f0f0 0%,#f7f7f7 60%,#ffffff 100%)}
  .deco-piece{position:absolute;background:linear-gradient(180deg,#e2e2e2,#ececec);opacity:.7;border-radius:40px 40px 8px 8px}
  .deco-left{left:24px;top:145px;width:82px;height:190px}
  .deco-right{left:722px;top:125px;width:100px;height:210px}
  .hero{position:absolute;left:100px;top:43px;width:418px;height:418px;border-radius:50%;border:5px solid #fff;background:radial-gradient(circle at 50% 45%,#fafafa 0%,#e6e6e6 70%,#d6d6d6 100%);overflow:hidden}
  .hero-figure{position:absolute;left:105px;top:30px;width:200px;height:350px;border-radius:60px 60px 30px 30px;background:linear-gradient(160deg,#3a3fd0 0%,#d43ab8 30%,#6fc0ea 55%,#f1d78a 80%,#c8cf4a 100%);opacity:.85}
  .title-ring{position:absolute;left:443px;top:95px;width:322px;height:322px;border-radius:50%;border:25px solid var(--blue);background:#fff;text-align:center}
  .title-ring h1{margin-top:64px;font-size:45px;font-weight:700;color:var(--blue);letter-spacing:.5px;line-height:1}
  .title-ring p{margin-top:8px;font-size:24px;line-height:30px;color:#222}
  .brand-disc{position:absolute;left:450px;top:308px;width:214px;height:214px;border-radius:50%;background:var(--blue);display:flex;align-items:center;justify-content:center}
  .brand-disc span{color:#fff;font-weight:700;font-size:28px;letter-spacing:1px}
  .headline{position:absolute;left:129px;top:546px;white-space:nowrap;font-size:31px;font-weight:700;color:var(--text);letter-spacing:-.3px}
  .headline em{font-style:normal;color:var(--blue)}
  .headline-rule{position:absolute;left:129px;top:591px;width:318px;height:2px;background:#444}
  .card{position:absolute;width:235px;height:105px;border-radius:7px;color:#fff;padding:7px 11px 0 11px;font-size:11px;line-height:14px;overflow:hidden}
  .card.blue{background:var(--blue)}
  .card.dark{background:var(--dark)}
  .card h3{font-size:12px;font-weight:700;display:inline-block;border-bottom:1px solid #fff;padding-bottom:1px;margin-bottom:5px;line-height:15px}
  .card p{text-align:justify;hyphens:auto;-webkit-hyphens:auto}
  .card.right{text-align:right}
  .card.right p{text-align:right}
  .slot{position:absolute;width:145px;height:93px;border:2px solid var(--frame);border-radius:8px;background:#fff}
  .notes{position:absolute;left:35px;top:1007px;width:515px;font-size:9.4px;line-height:13px;color:#444}
  .contact-band{position:absolute;left:0;top:1086px;width:560px;height:63px}
  .contact-line{position:absolute;left:14px;top:1109px;display:flex;align-items:center;gap:5px;font-size:13px;font-weight:700;color:#222;white-space:nowrap}
  .contact-line svg{width:12px;height:12px;fill:var(--blue)}
  .contact-line .gap{width:6px}
  .team{position:absolute;left:580px;top:990px;width:268px;height:200px;background:linear-gradient(180deg,#d9cfc6 0%,#5a5a5e 45%,#1e1e22 100%);border-radius:60px 60px 0 0}
  .base-stripe{position:absolute;left:0;top:1173px;width:848px;height:17px;background:var(--blue)}
</style>
</head>
<body>
<div class="flyer">
  <div class="top-wash"></div>
  <div class="deco-piece deco-left" role="img" aria-label="Faint chess piece in the background"></div>
  <div class="deco-piece deco-right" role="img" aria-label="Faint chess piece in the background"></div>

  <div class="hero">
    <div class="hero-figure" role="img" aria-label="Colourful splash illustration of a footballer with a ball"></div>
  </div>

  <div class="title-ring">
    <h1>VELKOR</h1>
    <p>Nachwuchsförderung<br>und -mangement</p>
  </div>
  <div class="brand-disc"><span>VELKOR</span></div>

  <h2 class="headline"><em>Wir begleiten dich</em> auf deinem Weg zum Profi</h2>
  <div class="headline-rule"></div>

  <div class="card blue" style="left:20px;top:615px">
    <h3>Karriereplanung</h3>
    <p>Wir haben deine Karriere im Blick! In enger Absprache mit deinen Eltern und dir leiten wir die richtigen Maßnahmen und Schritte ein, um dein Ziel „Profifußballer“ zu realisieren.</p>
  </div>
  <div class="slot" style="left:269px;top:621px"></div>
  <div class="slot" style="left:439px;top:621px"></div>
  <div class="card blue right" style="left:599px;top:615px">
    <h3>Ausrüstung</h3>
    <p>Wir besorgen dir deine Ausrüstung! Unsere Beziehungen zu den großen Sportartikelherstellern ermöglichenden Abschluss von Ausrüsterverträgen*.</p>
  </div>

  <div class="card dark" style="left:20px;top:741px">
    <h3>Ständiger Ansprechpartner</h3>
    <p>Egal um welchen Themen es sich handelt, wir sind für dich da! Ein vertrauensvolles und freundschaftliches Verhältnis ist uns besonders wichtig.</p>
  </div>
  <div class="slot" style="left:269px;top:747px"></div>
  <div class="slot" style="left:439px;top:747px"></div>
  <div class="card dark right" style="left:599px;top:741px">
    <h3>Vorsorge</h3>
    <p>Verletzungen gehören leider zum Fußball dazu. Wir sichern dich ab, indem wir eine private Zusatzkranken&shy;versicherung für dich abschließen.</p>
  </div>

  <div class="card blue" style="left:20px;top:873px">
    <h3>Rechtsberatung/Vertragsrecht</h3>
    <p>Juristendeutsch und Kleingedrucktes? Kein Problem! Wir helfen dir den Durchblick zu behalten und holen immer das Beste für dich raus.</p>
  </div>
  <div class="slot" style="left:269px;top:876px"></div>
  <div class="slot" style="left:439px;top:876px"></div>
  <div class="card blue right" style="left:599px;top:870px">
    <h3>Kooperationspartner/Netzwerk</h3>
    <p>Ob Entscheidungsträger oder Experte, wir kennen die richtigen Leute. Zusätzlich bieten wir dir eine große Bandbreite an Leistungen, die du jederzeit in Anspruch nehmen kannst**.</p>
  </div>

  <div class="notes">
    *Die Entscheidung über das Zustandekommen eines Ausrüstervertrags obliegt dem jeweiligen Sportartikelhersteller. Ist ein Abschluss aktuell nicht möglich, erhältst du von uns 2x pro Saison neue Fußballschuhe sowie weitere Ausrüstungsgegenstände.<br>
    **Personal Training, Athletik-Training, Ernährungsberatung, Sportpsychologische Betreuung, uvm.
  </div>

  <svg class="contact-band" viewBox="0 0 560 63" preserveAspectRatio="none" aria-hidden="true">
    <polygon points="0,0 560,0 498,63 0,63" fill="#dcdcdc"/>
  </svg>
  <div class="contact-line">
    <svg viewBox="0 0 24 24" aria-hidden="true"><path d="M6.6 10.8a15 15 0 0 0 6.6 6.6l2.2-2.2a1 1 0 0 1 1-.25 11.4 11.4 0 0 0 3.6.6 1 1 0 0 1 1 1V20a1 1 0 0 1-1 1A17 17 0 0 1 3 4a1 1 0 0 1 1-1h3.5a1 1 0 0 1 1 1c0 1.25.2 2.45.6 3.6a1 1 0 0 1-.25 1z"/></svg>
    <span>0123/4567890</span><span class="gap"></span>
    <svg viewBox="0 0 24 24" aria-hidden="true"><path d="M6 3h12v5H6zM4 9h16a2 2 0 0 1 2 2v6h-4v4H6v-4H2v-6a2 2 0 0 1 2-2zm4 7v3h8v-3z"/></svg>
    <span>0123/4567891</span>
    <svg viewBox="0 0 24 24" aria-hidden="true"><path d="M3 6h18v12H3zm2 2v.5l7 4.5 7-4.5V8l-7 4.5z"/></svg>
    <span>info@velkor-sport.de</span>
    <svg viewBox="0 0 24 24" aria-hidden="true"><circle cx="12" cy="12" r="9"/></svg>
    <span>www.velkor-sport.de</span>
  </div>

  <div class="team" role="img" aria-label="Photo of the three agency managers in dark suits"></div>
  <div class="base-stripe"></div>
</div>
</body>
</html>
```